Specialized Personal Trainer Needs a Business Card Design

I need a business card design for my personal training business called Tall Oak Fitness. I have my Human Kinetics degree in Exercise Science from the Halvern Ridge University as well as an extra certification from NBEP (National Board of Exercise Practice). I work as a Cardiac Rehab Exercise Specialist and personal trainer giving specialized exercise prescriptions to those that have different heart conditions as well as work with the general population in weight loss, strength and conditioning, getting/staying fit.
Updates

I decided that I wanted a logo (as I did not have one before I submitted my project for a business card) so I am submitting a project to get a logo done and then I will decide on a business card, hopefully being able to use one of the designs already submitted.  My apologies for doing this backwards.  I am new to this so I appreciate your patience.

Thank you.

Hi, I have just created a project for a logo design (I realized I needed a logo and I should've done that first..oops!), please feel free to participate.  Once I receive a logo I like I will finalize my business card project and hopefully incorporate it into one of your business card designs. 

Thank you!

Target Market(s)

Business professionals

Industry/Entity Type

Personal Trainer

Requirements
Must have
• My name with my info:
Celia R. Dunhill (BHK)
NBEP Certified Clinical Exercise Specialist & Personal Trainer
celia.dunhill@talloakfitness.example
Cell: 604-358-4170

Please make it double sided.
Nice to have
• An image that represents cardiac and general fitness training.

```html
<!DOCTYPE html>
<html lang="en">
<head>
<meta charset="utf-8">
<title>Tall Oak Fitness – Business Card</title>
<link rel="stylesheet" href="https://fonts.googleapis.com/css2?family=Quicksand:wght@400&family=Arimo:ital,wght@0,400;0,700;1,400&display=swap">
<style>
  :root {
    --stage-top: #4a4a4a;
    --stage-bottom: #141414;
    --card-white: #f4f4f4;
    --card-blue: #10a6f2;
    --card-blue-light: #3dbaf8;
    --brand-blue: #1a9de8;
    --brand-gold: #b89a63;
    --ink: #111111;
    --ink-soft: #3a3a3a;
    --wordmark-light: #f2f2f2;
    --rule-blue: #5cb8ee;
  }
  * { box-sizing: border-box; margin: 0; padding: 0; }
  html, body { width: 1192px; height: 1200px; overflow: hidden; }
  body {
    background: linear-gradient(180deg, var(--stage-top) 0%, #2a2a2a 55%, var(--stage-bottom) 100%);
    font-family: "Arimo", Arial, sans-serif;
    position: relative;
  }

  .brand-lockup {
    display: flex;
    align-items: center;
    gap: 18px;
  }
  .brand-mark {
    width: 1em;
    height: 1em;
    background: var(--brand-gold);
    flex: none;
  }
  .brand-name {
    font-family: "Quicksand", "Century Gothic", sans-serif;
    font-weight: 400;
    white-space: nowrap;
    line-height: 1;
  }

  .hero-lockup {
    position: absolute;
    top: 140px;
    left: 0;
    width: 100%;
    justify-content: center;
    font-size: 92px;
    gap: 26px;
  }
  .hero-lockup .brand-name { color: var(--wordmark-light); font-size: 72px; }

  .card {
    position: absolute;
    left: 256px;
    width: 680px;
    height: 390px;
    border-radius: 4px;
    box-shadow: 0 18px 40px rgba(0,0,0,0.45);
  }

  .card-front {
    top: 300px;
    background: var(--card-white);
  }
  .card-front .brand-lockup {
    position: absolute;
    top: 70px;
    left: 70px;
    font-size: 52px;
    gap: 16px;
  }
  .card-front .brand-name { color: var(--ink); font-size: 44px; }

  .contact-block {
    position: absolute;
    left: 350px;
    top: 210px;
    padding-left: 26px;
    border-left: 1px solid var(--rule-blue);
  }
  .contact-name { font-weight: 700; font-size: 18px; color: var(--ink); margin-bottom: 8px; }
  .contact-title {
    font-style: italic;
    font-size: 15px;
    line-height: 1.3;
    color: var(--brand-blue);
    margin-bottom: 18px;
  }
  .contact-line { font-size: 14px; line-height: 1.4; color: var(--ink-soft); }

  .card-back {
    top: 745px;
    background: linear-gradient(160deg, var(--card-blue-light) 0%, var(--card-blue) 60%, #0a97e0 100%);
  }
  .card-back .brand-lockup {
    position: absolute;
    top: 120px;
    left: 90px;
    font-size: 56px;
    gap: 16px;
  }
  .card-back .brand-name { color: #0b3550; font-size: 46px; }
  .web-address {
    position: absolute;
    top: 215px;
    left: 90px;
    font-size: 16px;
    color: #0b2a40;
  }
</style>
</head>
<body>

  <div class="brand-lockup hero-lockup">
    <span class="brand-mark"></span>
    <span class="brand-name">Tall Oak Fitness</span>
  </div>

  <section class="card card-front" aria-label="Business card front">
    <div class="brand-lockup">
      <span class="brand-mark"></span>
      <span class="brand-name">Tall Oak Fitness</span>
    </div>
    <div class="contact-block">
      <p class="contact-name">Celia R. Dunhill (BHK)</p>
      <p class="contact-title">NBEP Certified Clinical Exercise<br>Specialist &amp; Personal Trainer</p>
      <p class="contact-line">celia.dunhill@talloakfitness.example</p>
      <p class="contact-line">Cell: 604-358-4170</p>
    </div>
  </section>

  <section class="card card-back" aria-label="Business card back">
    <div class="brand-lockup">
      <span class="brand-mark"></span>
      <span class="brand-name">Tall Oak Fitness</span>
    </div>
    <p class="web-address">www.talloakfitness.example</p>
  </section>

</body>
</html>
```